World leading Water filters German made

I am a local Plumbing business who is authorised water filter installer
I want to do a Flyer design double sided targeting niche market for Water Filters.
My company colours are black background with white writing.
( but happy to go into different colours to capture more people )
I want all my stuff, sleek and professional with the same fonts throughout.
Www.brightvalepipeworks.au
Is my website you can see how I do things there.
I want the local business awards finalist logo on the flyer too ( it’ll be in the photo)
This Flyer I want all about health and wellness making big points on water filtration benefits
Massive to included HYDROGEN WATER AND ALKALINE WATER ,
REMOVE FLUORIDE
I don’t know whether to have it with the pre-save branded information I sent over, but I don’t want the company other companies name everywhere
I want the main focus about my company Brightvale Pipeworks And Boiler Experts
I want the focus to be about a family owned and run Illawarra local business establish for over 20 years.
Please note I have included a Customer brochure the company has designed so you can see some key points on the second page about the products. I want this a lot more eye-catching and appealing please
Target Market(s)
Health and wellness people
Colors
Designer to choose colors to be used in the design.
Requirements
Must have
- Call Trevor 0438 627 195, my website , social media buttons ,
Nice to have
- World leading , health and wellness ,
Should not have
- Any information to lead them away from calling myself , I’m the authorities dealer for purestream supply but I want to no have as much anout them.

```html
<!DOCTYPE html>
<html lang="en">
<head>
<meta charset="utf-8">
<title>Brightvale Pipeworks – Flyer</title>
<link href="https://fonts.googleapis.com/css2?family=Michroma&family=Open+Sans:wght@400;600;700&display=swap" rel="stylesheet">
<style>
:root{
  --red:#e3101c;
  --red-dark:#b80d17;
  --black:#111;
  --charcoal:#2a2a2c;
  --white:#fff;
  --grey:#555;
  --paper:#f4f4f4;
  --gold:#c9a455;
  --steel:#a9adb2;
}
*{margin:0;padding:0;box-sizing:border-box}
html,body{width:674px;height:1200px;overflow:hidden;background:var(--paper)}
body{position:relative;font-family:"Open Sans",Arial,sans-serif;color:var(--black)}
.flyer{position:absolute;left:132px;width:410px;height:580px;background:var(--white);overflow:hidden;box-shadow:0 2px 10px rgba(0,0,0,.18)}
.flyer--services{top:13px}
.flyer--health{top:607px}
.abs{position:absolute}
.header-photo{position:absolute;left:0;top:0;width:410px;height:225px;background:linear-gradient(135deg,#3a3a3d,#1b1b1d 60%,#2e2e31)}
.shape{position:absolute;left:0;width:410px}
.brand{position:absolute;left:12px;top:14px;display:flex;align-items:center;gap:6px;color:var(--white);font-family:"Michroma",sans-serif;font-size:7.5px;line-height:1.3;text-transform:uppercase}
.brand__mark{width:12px;height:12px;background:var(--white);flex:none}
.award{position:absolute;right:20px;top:0;width:52px;height:112px;background:var(--red)}
.award__medal{position:absolute;left:-7px;top:20px;width:66px;height:66px;border-radius:50%;background:radial-gradient(circle at 40% 35%,#f3dd9c,var(--gold) 60%,#8f6f2a)}
.award__bar{position:absolute;left:6px;right:6px;height:3px;background:rgba(255,255,255,.75)}
.headline{font-family:"Michroma",sans-serif;color:var(--white);font-size:17.5px;line-height:1.28;letter-spacing:-.2px;text-transform:uppercase}
.headline .accent{color:var(--red)}
.lede{color:var(--white);font-weight:700;font-size:9px;line-height:1.5}
.photo{position:absolute;background:linear-gradient(160deg,#d6d9dc,var(--steel) 50%,#6f7378)}
.section-title{font-family:"Michroma",sans-serif;color:var(--red);font-size:13px;letter-spacing:-.2px}
.services-title{font-family:"Michroma",sans-serif;color:var(--white);font-size:14px}
.service{position:absolute;width:104px}
.service__img{position:relative;width:100px;height:70px;background:linear-gradient(150deg,#cfd2d5,#8a8e93);overflow:hidden}
.service__img::after{content:"";position:absolute;left:0;bottom:0;width:100%;height:26px;background:var(--red);clip-path:polygon(0 35%,100% 0,100% 100%,0 100%)}
.service__label{position:absolute;left:4px;bottom:3px;z-index:1;color:var(--white);font-family:"Michroma",sans-serif;font-size:7px;line-height:1.3}
.service__text{margin-top:7px;font-size:6.4px;line-height:1.35;color:var(--grey)}
.perks{position:absolute;left:12px;top:496px;display:flex;gap:11px}
.perk{display:flex;align-items:center;gap:4px;font-size:6px;line-height:1.2;text-transform:uppercase;color:var(--black)}
.perk__icon{width:20px;height:20px;border-radius:50%;background:var(--charcoal);display:flex;align-items:center;justify-content:center}
.social{display:flex;gap:3px}
.social span{width:8px;height:8px;border-radius:50%;border:1.2px solid var(--white);display:block}
.cta-label{font-family:"Michroma",sans-serif;font-size:11px;color:var(--white)}
.cta-phone{font-family:"Michroma",sans-serif;font-size:15px;color:var(--red);letter-spacing:-.3px;display:flex;align-items:center;gap:4px;white-space:nowrap}
.site{font-size:6.5px;color:var(--white);white-space:nowrap}
.benefits{position:absolute;left:12px;top:248px;display:grid;grid-template-columns:112px 112px;row-gap:9px}
.benefit{display:flex;align-items:center;gap:6px;font-size:6.4px;line-height:1.25;color:var(--black)}
.benefit__icon{width:19px;height:19px;border-radius:50%;border:1.4px solid var(--red);flex:none}
.ticks{list-style:none;font-size:6.3px;line-height:1.55;color:var(--black);white-space:nowrap}
.ticks li::before{content:"✓";display:inline-block;width:6px;height:6px;border:.6px solid #777;border-radius:50%;font-size:4px;line-height:5.5px;text-align:center;margin-right:3px;vertical-align:1px;color:#555}
.cols{display:flex;gap:12px}
</style>
</head>
<body>

<!-- Side one: services -->
<section class="flyer flyer--services">
  <div class="header-photo" role="img" aria-label="Dark photo of hot water cylinders in a storeroom"></div>
  <div class="brand"><span class="brand__mark"></span><span>Brightvale Pipeworks<br>And Boiler Experts</span></div>
  <div class="award" role="img" aria-label="Local business awards finalist badge">
    <div class="award__medal"></div>
    <div class="award__bar" style="top:93px"></div>
    <div class="award__bar" style="top:100px;height:2px"></div>
  </div>
  <h1 class="headline abs" style="left:12px;top:72px">Your true<br>local plumber &amp;<br><span class="accent">hot water specialist</span></h1>
  <p class="lede abs" style="left:12px;top:148px;width:300px">We provide same day plumbing service throughout the Illawarra, Wollongong, Shellharbour &amp; Shoalhaven areas.</p>
  <div class="photo" style="left:322px;top:130px;width:80px;height:110px" role="img" aria-label="Stainless steel water filter unit mounted on a wall"></div>
  <svg class="shape" style="top:180px" width="410" height="70" viewBox="0 0 410 70" aria-hidden="true">
    <polygon points="0,10 240,0 410,28 410,40 0,40" fill="var(--red)"/>
    <polygon points="0,40 410,40 410,48 0,48" fill="var(--white)"/>
  </svg>
  <h2 class="services-title abs" style="left:12px;top:199px">SERVICES</h2>

  <div class="service" style="left:12px;top:245px"><div class="service__img" role="img" aria-label="Plumbing pipework photo"><span class="service__label">Plumbing<br>Maintenance</span></div><p class="service__text">As plumbing specialists, we guarantee expert installations and swift repairs.</p></div>
  <div class="service" style="left:154px;top:245px"><div class="service__img" role="img" aria-label="Hot water heat pump photo"><span class="service__label">Hot Water<br>Systems</span></div><p class="service__text">Trust the hot water specialists for all your installations.</p></div>
  <div class="service" style="left:296px;top:245px"><div class="service__img" role="img" aria-label="Hot water unit servicing photo"><span class="service__label">Hot Water<br>Servicing</span></div><p class="service__text">Trust our skilled plumbers for prompt and reliable hot water servicing.</p></div>
  <div class="service" style="left:12px;top:361px"><div class="service__img" role="img" aria-label="Drain camera inspection photo"><span class="service__label">Blocked Drains</span></div><p class="service__text">As plumbing specialists, we guarantee expert and swift results.</p></div>
  <div class="service" style="left:154px;top:361px"><div class="service__img" role="img" aria-label="Thermal camera leak detection photo"><span class="service__label">Leak Detection</span></div><p class="service__text">Let us help find and fix leaks throughout your plumbing.</p></div>
  <div class="service" style="left:296px;top:361px"><div class="service__img" role="img" aria-label="Water filter installation photo"><span class="service__label">Water Filters</span></div><p class="service__text">Our team can supply and install your new water filtration system.</p></div>

  <h2 class="section-title abs" style="left:12px;top:472px;font-size:13.5px">WHY CHOOSE US?</h2>
  <div class="perks">
    <div class="perk"><span class="perk__icon"><svg width="11" height="11" viewBox="0 0 12 12"><circle cx="6" cy="6" r="4.5" fill="none" stroke="#fff" stroke-width="1.2"/><path d="M6 3.5V6l2 1.2" fill="none" stroke="#fff" stroke-width="1.2"/></svg></span>Available<br>24/7</div>
    <div class="perk"><span class="perk__icon"><svg width="11" height="11" viewBox="0 0 12 12"><rect x="3" y="2" width="6" height="8" fill="none" stroke="#fff" stroke-width="1.1"/><path d="M4.5 6l1 1 2-2" fill="none" stroke="#fff" stroke-width="1.1"/></svg></span>Fully<br>licensed<br>&amp; insured</div>
    <div class="perk"><span class="perk__icon"><svg width="11" height="11" viewBox="0 0 12 12"><circle cx="4" cy="4" r="1.6" fill="#fff"/><circle cx="8" cy="4" r="1.6" fill="#fff"/><path d="M1.5 10a2.5 2.5 0 015 0M5.5 10a2.5 2.5 0 015 0" fill="#fff"/></svg></span>Family<br>run local<br>business</div>
    <div class="perk"><span class="perk__icon"><svg width="11" height="11" viewBox="0 0 12 12"><rect x="2" y="2.5" width="8" height="7" fill="none" stroke="#fff" stroke-width="1.1"/><path d="M3.5 5h5M3.5 7h3" stroke="#fff" stroke-width="1"/></svg></span>Lifetime<br>labour<br>warranty</div>
    <div class="perk"><span class="perk__icon"><svg width="11" height="11" viewBox="0 0 12 12"><circle cx="6" cy="6" r="4.5" fill="none" stroke="#fff" stroke-width="1.1"/><text x="6" y="8.2" font-size="6" text-anchor="middle" fill="#fff" font-family="Arial">$</text></svg></span>Fixed<br>upfront<br>pricing</div>
  </div>

  <svg class="shape" style="top:530px" width="410" height="50" viewBox="0 0 410 50" aria-hidden="true">
    <polygon points="0,50 0,38 410,0 410,50" fill="var(--black)"/>
    <polygon points="0,38 240,16 0,50" fill="var(--red)"/>
  </svg>
  <p class="cta-label abs" style="right:14px;top:542px">CALL TREVOR</p>
  <p class="cta-phone abs" style="right:12px;top:555px">0438 627 195
    <svg width="9" height="9" viewBox="0 0 12 12"><path d="M3 1l2 2.5-1.2 1.3a7 7 0 003.4 3.4L8.5 7 11 9l-1.5 2C5 11 1 7 1 2.5z" fill="#fff"/></svg></p>
  <p class="site abs" style="left:118px;top:563px">www.brightvalepipeworks.au</p>
  <div class="social abs" style="left:12px;top:563px" aria-label="Social media links"><span></span><span></span><span></span></div>
</section>

<!-- Side two: health and wellness -->
<section class="flyer flyer--health">
  <div class="header-photo" style="height:215px" role="img" aria-label="Dark photo of under-sink filtration plumbing"></div>
  <div class="brand"><span class="brand__mark"></span><span>Brightvale Pipeworks<br>And Boiler Experts</span></div>
  <div class="award" role="img" aria-label="Local business awards finalist badge">
    <div class="award__medal"></div>
    <div class="award__bar" style="top:93px"></div>
    <div class="award__bar" style="top:100px;height:2px"></div>
  </div>
  <h1 class="headline abs" style="left:12px;top:80px;font-size:18.5px">Hydrogen water<br>&amp; alkaline water,<br><span class="accent">remove fluoride</span></h1>
  <p class="lede abs" style="left:12px;top:153px;font-size:10px">a sustainable water filtration solution</p>
  <svg class="shape" style="top:170px" width="410" height="60" viewBox="0 0 410 60" aria-hidden="true">
    <polygon points="0,32 200,12 260,0 260,30 0,48" fill="var(--red)"/>
    <polygon points="0,48 260,30 410,30 410,60 0,60" fill="var(--white)"/>
  </svg>
  <div class="photo" style="left:222px;top:162px;width:180px;height:210px;border-radius:0 0 40px 40px" role="img" aria-label="Stainless steel whole-house filter unit with pressure gauges"></div>

  <h2 class="section-title abs" style="left:12px;top:226px">Health Benefits</h2>
  <div class="benefits">
    <div class="benefit"><span class="benefit__icon"></span>Reduce the risk of<br>cancer</div>
    <div class="benefit"><span class="benefit__icon"></span>Relief for asthma<br>sufferers</div>
    <div class="benefit"><span class="benefit__icon"></span>Relief for eczema<br>sufferers</div>
    <div class="benefit"><span class="benefit__icon"></span>Enjoy chemical<br>free showering</div>
    <div class="benefit"><span class="benefit__icon"></span>Anti-Aging<br>benefits</div>
    <div class="benefit"><span class="benefit__icon"></span>Healthier drinking<br>water</div>
    <div class="benefit"><span class="benefit__icon"></span>Reduce the risk of<br>birth defects</div>
  </div>

  <h2 class="section-title abs" style="left:12px;top:375px">Remove &amp; Improve</h2>
  <div class="cols abs" style="left:12px;top:394px">
    <ul class="ticks" style="width:86px"><li>Chlorine 99.99%</li><li>Chloramine 99.99%</li><li>Fluoride</li></ul>
    <ul class="ticks" style="width:58px"><li>Heavy Metals</li><li>Bacteria</li><li>Parasites</li></ul>
    <ul class="ticks"><li>Pesticides</li><li>Hard Water</li><li>PFA'S</li></ul>
  </div>
  <h2 class="section-title abs" style="left:252px;top:375px">Extend the life</h2>
  <div class="cols abs" style="left:252px;top:394px;gap:10px">
    <ul class="ticks"><li>Hot Water Systems</li><li>Washing machine</li><li>Dishwasher</li><li>Tapware</li></ul>
    <ul class="ticks"><li>Bathrooms</li><li>Plumbing</li><li>Home appliances</li></ul>
  </div>

  <div class="photo" style="left:12px;top:438px;width:218px;height:96px;background:linear-gradient(90deg,#c9ccd0,#8d9196 30%,#4a6ea8 55%,#eef0f2 75%,#d7d9dc)" role="img" aria-label="Filter housing, replacement cartridges and under-sink tap kit"></div>

  <h2 class="section-title abs" style="left:252px;top:441px">World Leading</h2>
  <ul class="ticks abs" style="left:252px;top:459px;line-height:1.5"><li>Australian, German &amp; Japanese Designed</li><li>100% Renewable</li><li>100% Sustainable</li><li>1000% Greater Absorption</li><li>Robust Design</li><li>Robust Warranty</li><li>Adopted throughout Europe and the USA</li></ul>

  <svg class="shape" style="top:532px" width="410" height="48" viewBox="0 0 410 48" aria-hidden="true">
    <polygon points="0,10 250,0 410,14 410,48 0,48" fill="var(--red)"/>
    <polygon points="290,48 410,30 410,48" fill="var(--black)"/>
  </svg>
  <p class="cta-label abs" style="left:12px;top:546px;font-size:10px">CALL TREVOR</p>
  <p class="cta-phone abs" style="left:12px;top:558px;color:var(--white)">
    <svg width="9" height="9" viewBox="0 0 12 12"><path d="M3 1l2 2.5-1.2 1.3a7 7 0 003.4 3.4L8.5 7 11 9l-1.5 2C5 11 1 7 1 2.5z" fill="#fff"/></svg>0438 627 195</p>
  <p class="site abs" style="left:186px;top:565px">www.brightvalepipeworks.au</p>
  <div class="social abs" style="right:12px;top:564px" aria-label="Social media links"><span></span><span></span><span></span></div>
</section>

</body>
</html>
```